依頼詳細
近隣のタワーマンションや、ホテル、貸会議室など、中高年層方々向けにチラシを置いてもらう、紹介してもらおうと考えております。シンプル、シックで上品な感じ、尚且つ、目を引く雰囲気にしていただけたらと思います。
記載項目
店名/Lorendal ロレンダール イタリアンダイニングレストラン
電話番号/06-6481-5926
住所:大阪市中央区緑岡町5-4-1 ミネハ紡第三ビル 地下1階
営業時間(Lunch:11:45-14:00、Dinner:17:30~23:30)
ランチメニュー【パスタランチ】¥800~
ディナーメニュー (アンティパスト¥1000~、ピザ.パスタ ¥1400~ お肉、お魚料理 ¥1800~、デザート¥600~)
添付写真イメージ
サイズ
A6
ページ数
両面
希望イメージ
シンプル 複雑
単色 カラフル
暗い 明るい
日常 高級
遊び心 厳粛
未来的 伝統的
女性的 男性的
希望する色
黒、白、ゴールド、木目などの茶色
納品ファイル
• 高解像度JPG (.jpg)
• イラストレーター形式 (.ai)
補足説明
写真や地図などは多少修正して頂いても、使わなくても結構です。
地図は添付の写真を参考にしていただければと思います。
とにかく、わかりやすく、ウリが的確に伝わるようにお願い致します。

```html
<!DOCTYPE html>
<html lang="ja">
<head>
<meta charset="utf-8">
<title>Lorendal — Italian Dining Restaurant</title>
<link rel="stylesheet" href="https://fonts.googleapis.com/css2?family=Cormorant+Garamond:ital,wght@0,400;0,500;1,400&family=Noto+Serif+JP:wght@400&display=swap">
<style>
  :root {
    --paper: #ffffff;
    --ink: #3a3a3a;
    --rule: #8a8a8a;
    --title-light: #f4efe6;
    --room-dark: #1a0e08;
    --room-mid: #4a2410;
    --room-glow: #b5561c;
    --wood: #6a3a1c;
  }
  html, body {
    margin: 0;
    padding: 0;
    width: 817px;
    height: 1200px;
    overflow: hidden;
    background: var(--paper);
  }
  .flyer-front {
    position: relative;
    width: 817px;
    height: 1200px;
    background: var(--paper);
  }
  .hero-photo {
    position: absolute;
    left: 0;
    top: 0;
    width: 817px;
    height: 830px;
    background:
      radial-gradient(ellipse 60% 30% at 50% 22%, rgba(230, 130, 50, 0.55), transparent 70%),
      radial-gradient(ellipse 30% 40% at 4% 38%, rgba(200, 70, 30, 0.55), transparent 70%),
      linear-gradient(180deg, var(--room-dark) 0%, var(--room-mid) 22%, var(--room-glow) 36%, var(--room-dark) 50%, var(--wood) 72%, var(--room-dark) 100%);
  }
  .hero-title {
    position: absolute;
    left: 0;
    right: 0;
    top: 28px;
    margin: 0;
    text-align: center;
    font-family: "Cormorant Garamond", serif;
    font-weight: 500;
    font-size: 30px;
    letter-spacing: 0.32em;
    color: var(--title-light);
  }
  .brand {
    position: absolute;
    left: 0;
    right: 0;
    top: 920px;
    text-align: center;
  }
  .brand-name {
    margin: 0;
    font-family: "Cormorant Garamond", serif;
    font-style: italic;
    font-weight: 400;
    font-size: 112px;
    line-height: 1;
    letter-spacing: 0.06em;
    color: var(--ink);
  }
  .brand-rule {
    width: 490px;
    height: 1px;
    margin: 18px auto 10px;
    background: var(--rule);
  }
  .brand-kana {
    margin: 0;
    font-family: "Noto Serif JP", serif;
    font-size: 19px;
    letter-spacing: 0.55em;
    color: var(--ink);
  }
</style>
</head>
<body>
  <main class="flyer-front">
    <div class="hero-photo" role="img" aria-label="Warmly lit restaurant interior with arched wall niches, a long bar counter and wooden tables set with cutlery"></div>
    <h2 class="hero-title">Italian Dining Restaurant</h2>
    <section class="brand">
      <h1 class="brand-name">Lorendal</h1>
      <div class="brand-rule"></div>
      <p class="brand-kana">イタリアン　ダイニング　レストラン</p>
    </section>
  </main>
</body>
</html>
```